Slider needed for Database Documentation Topic

We need a slider to promote a content area of a web site. I'm listing this as a poster because the posters I have seen on Quillbarn portfolios most closely resemble the combination or art and text I am looking for.
The content area we are promoting with this graphic will clarify the design and use of a complicated database. The title of the content area is "The Marbled QZ Database" and the banner should use that title.
To 'illuminate' something means to cast light on it, and this content area will help shed light on a complicated thing – the content will use diagrams, text, and examples to clarify the database. Another meaning is that an illuminated manuscript is a manuscript brought to life with pictures, and in a way that is also what this content area will do.
One idea for the slider might be a light bulb, lamp, candle or flashlight lighting up the words "QZ Database". Another idea would be the type of illustration you see if you search for "Illuminated manuscript"
But I'm not committed to any particular idea - in the past I have been pleased to see ideas that are different than my own but accomplish the same thing, so please feel free to use your judgement or ask any questions.
In addition to the title (The Marbled QZ Database) the graphic should allow room for three smaller lines of text – the three bullet items below:
- Guide to understanding the QZ database
- Data sources, uses and relationships explained with illustrations
- New content! Customers
The last bullet item will change as the content is added.
Some particulars ...
SIZE - 600 high x 1200 wide pixels
PHOTOS vs ILLUSTRATION - I am open to either one.

```html
<!DOCTYPE html>
<html lang="en">
<head>
<meta charset="utf-8">
<title>The Marbled QZ Database</title>
<link rel="stylesheet" href="https://fonts.googleapis.com/css2?family=Great+Vibes&family=EB+Garamond:wght@600&display=swap">
<style>
  :root {
    --night: #050403;
    --ink: #15110c;
    --parchment-light: #ece5d4;
    --parchment-mid: #b9ad94;
    --parchment-dark: #6f624d;
    --parchment-edge: #d9cba8;
    --glow-amber: #e6a22a;
    --glow-deep: #8a4a0e;
  }
  * { margin: 0; padding: 0; box-sizing: border-box; }
  html, body { width: 1200px; height: 600px; overflow: hidden; background: var(--night); }
  .slider {
    position: relative;
    width: 1200px;
    height: 600px;
    background: var(--night);
    overflow: hidden;
  }
  .candle-photo {
    position: absolute;
    left: 0; top: 0;
    width: 410px; height: 600px;
    background:
      radial-gradient(ellipse 420px 520px at 200px 480px, var(--glow-amber) 0%, var(--glow-deep) 40%, rgba(40,18,4,0.6) 70%, transparent 100%),
      var(--night);
  }
  .scroll {
    position: absolute;
    left: 410px; top: 25px;
    width: 770px; height: 555px;
  }
  .scroll svg { display: block; }
  .title {
    position: absolute;
    left: 415px; width: 760px;
    top: 92px;
    text-align: center;
    font-family: "Great Vibes", cursive;
    font-size: 52px;
    font-weight: 400;
    word-spacing: 12px;
    color: var(--ink);
    line-height: 1;
  }
  .bullets {
    position: absolute;
    left: 480px; top: 208px;
    width: 700px;
    list-style: none;
    font-family: "EB Garamond", serif;
    font-weight: 600;
    font-size: 32px;
    color: var(--ink);
    line-height: 40px;
  }
  .bullets li {
    position: relative;
    padding-left: 53px;
    white-space: nowrap;
  }
  .bullets li + li { margin-top: 54px; }
  .bullets li + li + li { margin-top: 35px; }
  .bullets .line { display: block; }
  .bullets .line.indent { margin-left: 57px; }
  .bullet-mark {
    position: absolute;
    left: 6px; top: 6px;
    width: 20px; height: 28px;
    border-radius: 50% 50% 50% 50% / 70% 70% 30% 30%;
    background: var(--ink);
  }
</style>
</head>
<body>
<main class="slider">
  <div class="candle-photo" role="img" aria-label="Photograph of a lit yellow wax candle glowing in the dark"></div>

  <div class="scroll">
    <svg width="770" height="555" viewBox="0 0 770 555" aria-hidden="true">
      <defs>
        <radialGradient id="parchment-fill" cx="0.52" cy="0.28" r="0.8">
          <stop offset="0" stop-color="#ece5d4"/>
          <stop offset="0.45" stop-color="#b9ad94"/>
          <stop offset="1" stop-color="#6f624d"/>
        </radialGradient>
      </defs>
      <path d="M20 22 L70 14 L78 30 L120 8 L190 18 L205 4 L260 16 L330 10 L345 24 L420 6 L470 16 L490 2 L560 14 L600 8 L612 22 L680 10 L720 20 L752 6 L742 60 L758 100 L744 150 L760 210 L748 260 L762 320 L746 380 L758 430 L744 480 L752 540 L700 530 L660 546 L600 534 L560 548 L500 536 L430 550 L380 536 L320 548 L260 534 L200 546 L150 532 L90 548 L40 532 L14 545 L26 480 L10 420 L24 370 L8 320 L22 260 L6 200 L20 150 L4 90 L18 60 Z"
            fill="url(#parchment-fill)" stroke="#d9cba8" stroke-width="5" stroke-linejoin="round"/>
    </svg>
  </div>

  <h1 class="title">The Marbled QZ Database</h1>

  <ul class="bullets">
    <li><span class="bullet-mark" aria-hidden="true"></span>Guide to understanding the QZ database</li>
    <li><span class="bullet-mark" aria-hidden="true"></span><span class="line">Data sources, uses and relationships</span><span class="line indent">explained with illustrations</span></li>
    <li><span class="bullet-mark" aria-hidden="true"></span>New content! Customers</li>
  </ul>
</main>
</body>
</html>
```